Vemtri Gymnastics Cobalt Gym banner

We need a banner for our new gym.
It should have navy, light blue, lilac and purple colors with our name, logo and other wording in navy color. Colors should bleed one into the other.
File with name, logo and other wording is attached.
Words: Rhythmic gymnastics, ballet, etc should be on the bottom

Target Market(s)

Girls 3 to 16 years of age

Industry/Entity Type

Athletics

Font styles to use
Other font styles liked:
• Please use fonts on file included

Colors
0054AA
0677BA
7BADD7
CADEEF
E8F1F8
0094D4
00A9DD
6FCCEA
C7EBF8
E9F6FB
00AB8E
00BBA5
67D7C9
C6EFE9
E9F9F6
6B429C
8869AF
B7A5CE
E3DAEB
F3F0F8

Requirements
Must have
• our logo and name of the gym
Nice to have
• rhythmic gymnastics feel
Should not have
• bold colors

```html
<!DOCTYPE html>
<html lang="en">
<head>
<meta charset="utf-8">
<title>Vemtri Gymnastics – Cobalt Gym Banner</title>
<link href="https://fonts.googleapis.com/css2?family=Tinos:wght@400;700&display=swap" rel="stylesheet">
<style>
  :root {
    --page-bg: #e4e4e6;
    --banner-left: #6d5fd6;
    --banner-mid: #3a3cc0;
    --banner-right: #1c27a6;
    --navy: #0f1e96;
    --navy-ring: #1d2aa8;
    --purple-glow: #9b64d6;
    --purple-deep: #7a3cbf;
    --lilac: #b186e8;
    --photo-light: #e6f6fb;
    --photo-edge: #c7ebf8;
    --white: #ffffff;
    --ink: #0f1e96;
  }
  html, body {
    margin: 0;
    width: 1119px;
    height: 1200px;
    overflow: hidden;
    background: var(--page-bg);
  }
  .canvas {
    width: 1119px;
    height: 1200px;
    display: flex;
    align-items: center;
    justify-content: center;
  }
  .banner {
    width: 1060px;
    height: 441px;
    display: block;
    box-shadow: 0 18px 30px rgba(0,0,0,0.28);
  }
  .banner text { font-family: "Tinos", "Times New Roman", serif; }
  .brand-name { font-size: 58px; font-weight: 400; fill: var(--white); }
  .brand-tagline { font-size: 19px; font-weight: 400; fill: var(--white); letter-spacing: 0.5px; }
  .gym-title { font-size: 112px; font-weight: 700; fill: var(--white); }
  .service-list { font-size: 22px; font-weight: 400; fill: var(--white); }
  .contact-text { font-size: 16px; font-weight: 700; fill: var(--ink); }
</style>
</head>
<body>
<main class="canvas">
  <svg class="banner" viewBox="0 0 1210 503" xmlns="http://www.w3.org/2000/svg" aria-label="Vemtri Gymnastics Cobalt Gym banner">
    <defs>
      <linearGradient id="bannerFade" x1="0" y1="0" x2="1" y2="0">
        <stop offset="0" stop-color="var(--banner-left)"/>
        <stop offset="0.5" stop-color="var(--banner-mid)"/>
        <stop offset="1" stop-color="var(--banner-right)"/>
      </linearGradient>
      <linearGradient id="purpleGlow" x1="0" y1="0" x2="1" y2="1">
        <stop offset="0" stop-color="var(--purple-glow)"/>
        <stop offset="1" stop-color="var(--purple-deep)"/>
      </linearGradient>
      <radialGradient id="photoTone" cx="0.5" cy="0.45" r="0.6">
        <stop offset="0" stop-color="var(--photo-light)"/>
        <stop offset="1" stop-color="var(--photo-edge)"/>
      </radialGradient>
      <clipPath id="bannerClip"><rect width="1210" height="503"/></clipPath>
    </defs>

    <g clip-path="url(#bannerClip)">
      <rect class="banner-bg" width="1210" height="503" fill="url(#bannerFade)"/>
      <rect class="navy-edge" x="1090" width="120" height="503" fill="var(--navy)"/>
      <circle class="brand-glow" cx="319" cy="90" r="285" fill="url(#purpleGlow)" opacity="0.85"/>

      <circle class="frame-ring-outer" cx="929" cy="170" r="280" fill="none" stroke="var(--white)" stroke-width="1.5"/>
      <circle class="frame-navy" cx="929" cy="170" r="268" fill="var(--navy-ring)"/>
      <circle class="photo" cx="929" cy="170" r="253" fill="url(#photoTone)" role="img" aria-label="Photo of a young rhythmic gymnast in a split, twirling a pink ribbon"/>
      <circle class="lilac-base" cx="924" cy="560" r="250" fill="var(--lilac)" opacity="0.95"/>
      <circle class="lilac-ring" cx="924" cy="560" r="272" fill="none" stroke="var(--white)" stroke-width="1.5"/>
      <circle class="photo-ring" cx="929" cy="170" r="262" fill="none" stroke="var(--white)" stroke-width="1.5"/>

      <text class="brand-name" x="326" y="88" text-anchor="middle" textLength="410" lengthAdjust="spacing">Vemtri Gymnastics</text>
      <text class="brand-tagline" x="527" y="121" text-anchor="end">Home of Young Stars</text>

      <circle class="brand-mark" cx="140" cy="240" r="62" fill="none" stroke="var(--white)" stroke-width="4"/>

      <text class="gym-title" x="242" y="242" textLength="300" lengthAdjust="spacingAndGlyphs">Cobalt</text>
      <text class="gym-title" x="342" y="330" textLength="242" lengthAdjust="spacingAndGlyphs">Gym</text>

      <text class="service-list" x="331" y="394" text-anchor="middle" xml:space="preserve">• Rhythmic Gymnastics | • Ballet | • Ballroom Dance</text>
      <text class="service-list" x="329" y="425" text-anchor="middle" xml:space="preserve">• Ballet | • Stretching | • Hip Hop</text>

      <g class="contact-bar">
        <rect x="132" y="446" width="386" height="30" rx="15" fill="var(--white)"/>
        <circle cx="148" cy="461" r="8" fill="var(--ink)"/>
        <path d="M144.5 456.5 q0 8 7 9 l1.5 -2 -2.5 -1.5 -1 1 q-2.5 -1 -3.5 -3.5 l1 -1 -1.5 -2.5z" fill="var(--white)"/>
        <text class="contact-text" x="160" y="467">(555) 014-2290 |</text>
        <circle cx="285" cy="461" r="8" fill="var(--ink)"/>
        <circle cx="285" cy="461" r="5" fill="none" stroke="var(--white)" stroke-width="1"/>
        <line x1="280" y1="461" x2="290" y2="461" stroke="var(--white)" stroke-width="1"/>
        <ellipse cx="285" cy="461" rx="2" ry="5" fill="none" stroke="var(--white)" stroke-width="1"/>
        <text class="contact-text" x="297" y="467">www.vemtrigymnastics.com</text>
      </g>
    </g>
  </svg>
</main>
</body>
</html>
```